Fernvale Business Card Design

We are looking for a fresh business card design for our new logo. We would like a business card that is unique but friendly. We are in the window coverings business offering blinds, shutters and shades for homes.

Target Market(s)

Targeting the end-consumer

Industry/Entity Type

Business

Requirements
Must have
• Must have a dedicates space for a photo of our sales person. Must contain our new logo (attached).

```html
<!DOCTYPE html>
<html lang="en">
<head>
<meta charset="utf-8">
<title>Fernvale Business Card</title>
<link rel="stylesheet" href="https://fonts.googleapis.com/css2?family=Marcellus&family=Open+Sans:wght@400;600&display=swap">
<style>
  :root {
    --bg: #2b2b2c;
    --green: #7cb342;
    --green-soft: #8bc34a;
    --slate: #5b5c5e;
    --slate-dark: #4a4b4d;
    --slate-light: #7a7b7d;
    --ink: #5f6062;
    --paper: #ffffff;
    --paper-shade: #e9eaea;
    --brand-light: #e6e6e6;
  }
  * { margin: 0; padding: 0; box-sizing: border-box; }
  html, body { width: 1200px; height: 900px; overflow: hidden; }
  body {
    background: var(--bg);
    font-family: "Open Sans", Arial, sans-serif;
    position: relative;
  }
  .card {
    position: absolute;
    left: 320px;
    width: 560px;
    height: 320px;
    border-radius: 0 26px 0 26px;
    overflow: hidden;
  }

  /* Back of card */
  .card-back {
    top: 80px;
    background: linear-gradient(135deg, var(--slate-light) 0%, var(--slate) 50%, var(--slate-dark) 100%);
  }
  .card-back .brand {
    position: absolute;
    left: 110px;
    top: 108px;
    display: flex;
    align-items: center;
    gap: 20px;
  }
  .brand-square {
    width: 64px;
    height: 64px;
    border: 4px solid var(--brand-light);
    border-radius: 6px;
  }
  .card-back .brand-name {
    font-family: "Marcellus", Georgia, serif;
    font-size: 66px;
    color: var(--brand-light);
    line-height: 1;
  }
  .card-back .website {
    position: absolute;
    left: 210px;
    top: 196px;
    font-size: 13px;
    color: var(--green);
  }
  .card-back .rule {
    position: absolute;
    left: 110px;
    right: 60px;
    top: 222px;
    height: 3px;
    background: var(--green);
  }

  /* Front of card */
  .card-front {
    top: 500px;
    background: linear-gradient(120deg, var(--paper) 0%, var(--paper) 55%, var(--paper-shade) 100%);
  }
  .accent-block {
    position: absolute;
    left: 0; top: 112px;
    width: 80px; height: 62px;
    background: var(--green-soft);
  }
  .accent-divider {
    position: absolute;
    left: 90px; top: 96px;
    width: 2px; height: 100px;
    background: var(--slate);
  }
  .card-front .brand {
    position: absolute;
    left: 104px; top: 118px;
    display: flex; align-items: center; gap: 10px;
  }
  .card-front .brand-square {
    width: 34px; height: 34px;
    border: 3px solid var(--ink);
    border-radius: 4px;
  }
  .card-front .brand-name {
    font-family: "Marcellus", Georgia, serif;
    font-size: 32px;
    color: var(--ink);
    line-height: 1;
  }
  .name-divider {
    position: absolute;
    left: 312px; top: 40px;
    width: 2px; height: 112px;
    background: var(--green);
  }
  .name-band {
    position: absolute;
    left: 320px; right: 0; top: 40px;
    height: 66px;
    background: var(--slate);
    text-align: right;
    padding: 8px 34px 0 0;
  }
  .person-name {
    font-size: 26px;
    color: var(--paper);
    line-height: 1.15;
  }
  .job-title {
    font-size: 13px;
    color: var(--green-soft);
  }
  .contact-list {
    position: absolute;
    right: 34px; top: 118px;
    list-style: none;
    text-align: right;
  }
  .contact-list li {
    font-size: 13px;
    color: var(--ink);
    height: 25px;
    display: flex; align-items: center; justify-content: flex-end; gap: 8px;
  }
  .contact-list svg { width: 12px; height: 12px; fill: var(--green); }
  .corner-block {
    position: absolute;
    right: 0; top: 200px;
    width: 44px; height: 24px;
    background: var(--slate);
  }
  .web-band {
    position: absolute;
    left: 290px; right: 52px; top: 228px;
    height: 26px;
    background: var(--green-soft);
    color: var(--paper);
    font-size: 13px;
    text-align: right;
    padding: 4px 14px 0 0;
  }
  .photo-slot {
    position: absolute;
    left: 116px; top: 192px;
    width: 190px; height: 128px;
    background: linear-gradient(180deg, #d8d4d0 0%, #8a8684 45%, #2f3032 100%);
  }
  .foot-band {
    position: absolute;
    left: 0; bottom: 14px;
    width: 116px; height: 14px;
    background: var(--green-soft);
  }
</style>
</head>
<body>

<section class="card card-back">
  <div class="brand">
    <span class="brand-square"></span>
    <span class="brand-name">Fernvale</span>
  </div>
  <p class="website">www.yourwebsite.com</p>
  <div class="rule"></div>
</section>

<section class="card card-front">
  <div class="accent-block"></div>
  <div class="accent-divider"></div>
  <div class="brand">
    <span class="brand-square"></span>
    <span class="brand-name">Fernvale</span>
  </div>

  <div class="name-divider"></div>
  <div class="name-band">
    <p class="person-name">Your Name</p>
    <p class="job-title">Job Title</p>
  </div>

  <ul class="contact-list">
    <li>000 000 0000
      <svg viewBox="0 0 24 24"><path d="M6.6 10.8a15 15 0 0 0 6.6 6.6l2.2-2.2c.3-.3.7-.4 1-.2 1.1.4 2.3.6 3.6.6.6 0 1 .4 1 1V20c0 .6-.4 1-1 1C10.6 21 3 13.4 3 4c0-.6.4-1 1-1h3.5c.6 0 1 .4 1 1 0 1.3.2 2.5.6 3.6.1.3 0 .7-.2 1z"/></svg>
    </li>
    <li>youremail@xyz.com
      <svg viewBox="0 0 24 24"><path d="M2 5h20v14H2z M2 5l10 8 10-8" fill="var(--green)"/><path d="M3 6l9 7 9-7" fill="none" stroke="#fff" stroke-width="1.5"/></svg>
    </li>
    <li>youraddress, here 0000
      <svg viewBox="0 0 24 24"><path d="M12 2a7 7 0 0 0-7 7c0 5 7 13 7 13s7-8 7-13a7 7 0 0 0-7-7zm0 9.5A2.5 2.5 0 1 1 12 6.5a2.5 2.5 0 0 1 0 5z"/></svg>
    </li>
  </ul>

  <div class="corner-block"></div>
  <div class="web-band">www.yourwebsite.com</div>

  <div class="photo-slot" role="img" aria-label="Photo of the sales person"></div>
  <div class="foot-band"></div>
</section>

</body>
</html>
```